Corvellan Hotel

A Hotel (Pub) in Sydney CBD. Posters will be outside of Hotel informing People what is on in Hotel.
We will be Printing in A1 size.
CORVELLAN HOTEL
Open 9am - 3am 7 Days
Monday - Thursday
Happy Hour
4pm - 6pm
Local Beer & Wine
Wednesday
Poker Night: Great $$$ Prizes
Everyday
Steak or Schniztels: Served with Mashed Potato & Salad or Chips & Salad - $8.50
Live Sport on the Big Screen
BISTRO
OPEN 7 DAYS 12- 9pm
Daily Blackboard Specials + Full Menu Inside
Best service in Town
Male or Female 18 to Seniors.Passing Trade.
Hotel

```html
<!DOCTYPE html>
<html lang="en">
<head>
<meta charset="utf-8">
<title>Corvellan Hotel – What's On</title>
<link rel="stylesheet" href="https://fonts.googleapis.com/css2?family=Anton&family=Arvo:wght@400;700&display=swap">
<style>
  :root {
    --navy: #0b2e45;
    --panel: #ffffff;
    --orange: #f58220;
    --ink: #111111;
    --body: #1a1a1a;
    --gold: #e0a21a;
    --swoosh: #ffffff;
    --brand: #9fb2bf;
  }
  * { box-sizing: border-box; margin: 0; padding: 0; }
  html, body { width: 848px; height: 1200px; overflow: hidden; background: var(--navy); }
  .poster {
    position: relative; width: 848px; height: 1200px; overflow: hidden;
    background: var(--navy);
    font-family: "Arvo", Georgia, serif;
  }
  .swooshes { position: absolute; inset: 0; width: 848px; height: 1200px; }
  .swooshes path { fill: none; }
  .feature {
    position: absolute; left: 61px; width: 724px;
    background: var(--panel); border-radius: 12px;
    box-shadow: 5px 6px 8px rgba(0,0,0,0.55);
  }
  .headline {
    position: absolute; left: 30px;
    font-family: "Anton", Impact, sans-serif;
    color: var(--orange);
    -webkit-text-stroke: 2.5px var(--ink);
    paint-order: stroke fill;
    letter-spacing: -0.5px;
    line-height: 1;
  }
  .detail {
    position: absolute; left: 32px;
    font-size: 19px; color: var(--body); line-height: 1.25;
  }
  .feature--happy { top: 78px; height: 160px; }
  .feature--poker { top: 262px; height: 162px; }
  .feature--sport { top: 447px; height: 162px; }
  .feature--bistro { top: 628px; height: 333px; }
  .feature--happy .headline { top: 14px; font-size: 92px; }
  .feature--happy .detail { top: 115px; }
  .feature--poker .headline { top: 14px; font-size: 92px; }
  .feature--poker .detail { top: 120px; }
  .feature--sport .headline { top: 14px; font-size: 92px; }
  .feature--sport .detail { top: 118px; }
  .feature--bistro .headline { top: 10px; font-size: 92px; line-height: 0.98; }
  .feature--bistro .detail--serve { top: 198px; }
  .bistro-info { position: absolute; left: 32px; top: 238px; font-size: 18px; line-height: 1.3; color: var(--body); }
  .bistro-info .label { font-weight: 700; font-size: 22px; letter-spacing: 0.5px; }
  .visual { position: absolute; }
  .visual--stopwatch { left: 556px; top: 8px; width: 118px; height: 146px;
    border-radius: 50% 50% 50% 50% / 44% 44% 56% 56%;
    background: radial-gradient(circle at 50% 60%, #f3efe6 0 48%, #b9b9b9 52%, #6f6f6f 70%); }
  .visual--cards { left: 500px; top: 16px; width: 212px; height: 142px; border-radius: 8px;
    background: linear-gradient(135deg, #f4f1ec 0%, #e6d7c4 40%, #c98d6a 100%); }
  .visual--screen { left: 510px; top: 19px; width: 188px; height: 127px; border-radius: 3px;
    background: linear-gradient(180deg, #222 0 6%, #596d3e 6% 45%, #3f8a34 45% 94%, #222 94%); }
  .visual--cutlery { left: 556px; top: 22px; width: 138px; height: 292px; border-radius: 30px;
    background: linear-gradient(90deg, #d8d8d8, #ffffff 30%, #a9a9a9 55%, #f1f1f1 80%, #bdbdbd); }
  .hours {
    position: absolute; left: 64px; top: 1004px;
    font-family: "Anton", Impact, sans-serif;
    font-size: 42px; line-height: 1.12; color: var(--orange);
    text-shadow: 3px 3px 3px rgba(0,0,0,0.7);
  }
  .brand {
    position: absolute; left: 560px; top: 1060px;
    font-family: "Arvo", Georgia, serif;
    font-size: 30px; color: var(--brand); line-height: 1.2;
  }
</style>
</head>
<body>
<main class="poster">
  <svg class="swooshes" viewBox="0 0 848 1200" aria-hidden="true">
    <path d="M560 0 C650 40 760 90 848 150" stroke="var(--gold)" stroke-width="3"/>
    <path d="M0 30 C250 10 620 40 848 110" stroke="var(--swoosh)" stroke-width="2"/>
    <path d="M610 0 C700 50 790 120 848 175" stroke="var(--swoosh)" stroke-width="2.5"/>
    <path d="M780 160 C810 190 830 220 848 245" stroke="var(--gold)" stroke-width="2"/>
    <path d="M790 250 C815 262 835 272 848 280" stroke="var(--swoosh)" stroke-width="2"/>
    <path d="M0 950 C120 1010 260 1080 380 1200" stroke="var(--gold)" stroke-width="3"/>
    <path d="M0 1030 C140 1060 330 1130 440 1200" stroke="var(--swoosh)" stroke-width="2.5"/>
    <path d="M0 1100 C200 1120 380 1160 470 1200" stroke="var(--swoosh)" stroke-width="2"/>
    <path d="M300 1180 C520 1150 700 1170 848 1140" stroke="var(--gold)" stroke-width="2.5"/>
    <path d="M380 1200 C560 1170 720 1190 848 1175" stroke="var(--swoosh)" stroke-width="2"/>
  </svg>

  <section class="feature feature--happy">
    <h2 class="headline">Happy Hour</h2>
    <p class="detail">4pm - 6pm. Mon - Thurs. Local Beer &amp; Wine</p>
    <div class="visual visual--stopwatch" role="img" aria-label="Photo of a silver stopwatch"></div>
  </section>

  <section class="feature feature--poker">
    <h2 class="headline">Poker Night</h2>
    <p class="detail">Every Wednesday. Great $$$ Prizes</p>
    <div class="visual visual--cards" role="img" aria-label="Photo of a hand holding four kings"></div>
  </section>

  <section class="feature feature--sport">
    <h2 class="headline">Live Sports</h2>
    <p class="detail">All your favourites on the Big Screen</p>
    <div class="visual visual--screen" role="img" aria-label="Photo of a flat screen showing a rugby match"></div>
  </section>

  <section class="feature feature--bistro">
    <h2 class="headline">$8.50 Steak<br>or Schnitzel</h2>
    <p class="detail detail--serve">Served with Mash &amp; Salad OR Chips &amp; Salad</p>
    <div class="bistro-info">
      <p class="label">BISTRO</p>
      <p>OPEN 7 DAYS. 12 - 9pm</p>
      <p>Daily Blackboard Specials + Full Menu Inside.</p>
    </div>
    <div class="visual visual--cutlery" role="img" aria-label="Photo of a silver fork, knife and spoon"></div>
  </section>

  <p class="hours">Open 7 Days<br>9am - 3am<br>Best Service in Town</p>

  <p class="brand">Corvellan Hotel</p>
</main>
</body>
</html>
```